2011 Pinot Noir
Yes
This goal of this project is to design a wine label for our new wine and winery in The Umpqua Valley AVA of southern Oregon. (An AVA is a designated wine region, such as Napa Valley). We are a small, boutique-style producer that will be making high end wines from grapes grown in our own vineyard. Our label should stand out and grab the eye in a sophisticated, stylish and elegant way and establish our wine as a unique artistic expression of a single piece of earth (the "Copperleaf Glen") that cannot be replicated. The target market for this wine is 35+ in age, middle-to-upper income, and curious and/or somewhat knowledgeable about wine.
The name "Copperleaf Glen" is a reference to the phrase "The Hundred Valleys of The Umpqua," which is how the Umpqua River Valley of Oregon is described. Rather than being a single, large river valley, it is a network of little, secluded valleys. Our vineyard is located within its own little hidden valley, a place we wish to distinguish as special, mystical, magical, and a source of premium grapes and quality wines.
Outdoors/Natural
Open to ideas but would like to print on ivory paper. Keep it simple and elegant.
not sure
http://snapcrate.example/copperleafglen
I have uploaded some images of our valley to snapcrate at the link above. These can be used as inspiration only or you can use them in whole or in part in the label design. You do not have to use these images, they are just an option.
Please email if you need a photo sent to you directly.
Illustrations are also welcome, as are other images you wish to use that are not copyright incumbered.
However, I do not want to see a "vineyard," "grapevine" or "grape" image on the label, nor do I want to see a "chateau."

```html
<!DOCTYPE html>
<html lang="en">
<head>
<meta charset="utf-8">
<title>Copperleaf Glen – 2011 Pinot Noir Labels</title>
<link rel="stylesheet" href="https://fonts.googleapis.com/css2?family=Cinzel:wght@400&family=Cormorant+Garamond:ital,wght@1,400&display=swap">
<style>
  :root {
    --page: #ffffff;
    --ivory: #eeefe6;
    --ink: #2b2b2b;
    --silver-top: #f2f2f2;
    --silver-bottom: #bdbdbd;
    --silver-ink: #4a4a4a;
    --claret-light: #b3202a;
    --claret-dark: #6e0c12;
    --claret-ink: #d9d9d9;
    --black: #0d0d0d;
    --black-ink: #e6e6e6;
    --black-mark-fill: #8a8a8a;
  }
  html, body {
    margin: 0;
    padding: 0;
    width: 1200px;
    height: 871px;
    overflow: hidden;
    background: var(--page);
  }
  .canvas {
    position: relative;
    width: 1200px;
    height: 871px;
  }
  .label {
    position: absolute;
    width: 47.8em;
    height: 66.7em;
    font-size: 10px;
    color: var(--label-ink);
    background: var(--label-bg);
    text-align: center;
  }
  .label--ivory  { --label-bg: var(--ivory); --label-ink: var(--ink); --mark-fill: transparent; left: 0; top: 0; }
  .label--silver { --label-bg: linear-gradient(180deg, var(--silver-top), var(--silver-bottom)); --label-ink: var(--silver-ink); --mark-fill: transparent; }
  .label--claret { --label-bg: radial-gradient(ellipse at 50% 35%, var(--claret-light), var(--claret-dark)); --label-ink: var(--claret-ink); --mark-fill: transparent; }
  .label--noir   { --label-bg: var(--black); --label-ink: var(--black-ink); --mark-fill: transparent; }
  .label--noir-filled { --mark-fill: var(--black-mark-fill); }

  .label--small { font-size: 6.13px; }
  .label--pos-a { left: 593px; top: 149px; }
  .label--pos-b { left: 895px; top: 149px; }
  .label--pos-c { left: 593px; top: 420px; }
  .label--pos-d { left: 895px; top: 420px; }

  .brand-mark {
    position: absolute;
    left: 0; right: 0;
    top: 5.5em;
    display: flex;
    justify-content: center;
    align-items: center;
    gap: 1.4em;
  }
  .brand-mark__square {
    width: 9em;
    height: 9em;
    border: 0.25em solid var(--label-ink);
    background: var(--mark-fill);
    box-sizing: border-box;
  }
  .brand-mark__name {
    font-family: "Cinzel", serif;
    font-weight: 400;
    font-size: 2.6em;
    letter-spacing: 0.05em;
    color: var(--label-ink);
  }
  .winery-name {
    position: absolute;
    left: 0; right: 0;
    top: 20.5em;
    margin: 0;
    font-family: "Cinzel", serif;
    font-weight: 400;
    font-size: 1em;
    line-height: 1;
  }
  .winery-name__line {
    display: block;
    font-size: 5.6em;
    letter-spacing: 0.03em;
    line-height: 1.05;
  }
  .vintage {
    position: absolute;
    left: 0; right: 0;
    top: 43.5em;
    font-family: "Cormorant Garamond", serif;
    font-style: italic;
    font-size: 1em;
  }
  .vintage span { font-size: 4.6em; letter-spacing: 0.06em; }
  .varietal {
    position: absolute;
    left: 0; right: 0;
    top: 55.5em;
    font-family: "Cinzel", serif;
    font-size: 1em;
  }
  .varietal span { font-size: 5em; letter-spacing: 0.02em; }
</style>
</head>
<body>
<main class="canvas">

  <article class="label label--ivory">
    <div class="brand-mark"><div class="brand-mark__square"></div><span class="brand-mark__name">Copperleaf Glen</span></div>
    <h1 class="winery-name"><span class="winery-name__line">Copperleaf</span><span class="winery-name__line">Glen</span></h1>
    <p class="vintage"><span>2011</span></p>
    <p class="varietal"><span>Pinot Noir</span></p>
  </article>

  <article class="label label--small label--silver label--pos-a">
    <div class="brand-mark"><div class="brand-mark__square"></div><span class="brand-mark__name">Copperleaf Glen</span></div>
    <h2 class="winery-name"><span class="winery-name__line">Copperleaf</span><span class="winery-name__line">Glen</span></h2>
    <p class="vintage"><span>2011</span></p>
    <p class="varietal"><span>Pinot Noir</span></p>
  </article>

  <article class="label label--small label--claret label--pos-b">
    <div class="brand-mark"><div class="brand-mark__square"></div><span class="brand-mark__name">Copperleaf Glen</span></div>
    <h2 class="winery-name"><span class="winery-name__line">Copperleaf</span><span class="winery-name__line">Glen</span></h2>
    <p class="vintage"><span>2011</span></p>
    <p class="varietal"><span>Pinot Noir</span></p>
  </article>

  <article class="label label--small label--noir label--noir-filled label--pos-c">
    <div class="brand-mark"><div class="brand-mark__square"></div><span class="brand-mark__name">Copperleaf Glen</span></div>
    <h2 class="winery-name"><span class="winery-name__line">Copperleaf</span><span class="winery-name__line">Glen</span></h2>
    <p class="vintage"><span>2011</span></p>
    <p class="varietal"><span>Pinot Noir</span></p>
  </article>

  <article class="label label--small label--noir label--pos-d">
    <div class="brand-mark"><div class="brand-mark__square"></div><span class="brand-mark__name">Copperleaf Glen</span></div>
    <h2 class="winery-name"><span class="winery-name__line">Copperleaf</span><span class="winery-name__line">Glen</span></h2>
    <p class="vintage"><span>2011</span></p>
    <p class="varietal"><span>Pinot Noir</span></p>
  </article>

</main>
</body>
</html>
```